依頼詳細
今回は、神戸市中央区周辺のお客様に対してのポルネット本町店に来店いただくためのチラシの作成をお願いいたします。

ポスティングを予定しておりますので、近隣住民の方に特に反応が高いような設計がベストとなります。

チラシの土台となるレターは添付ファイルをご確認ください。
記載項目
ポルネット本町店
火曜定休
月曜日~木曜日10:00~22:00
金曜日~日曜日10:00~18:00
TEL:078-415-3728

住所:
〒650-0011 兵庫県神戸市中央区下山手通5丁目8−21 ORB508ビル B1

URL:
https://polnetto-example.com

サイズ
A4
ページ数
片面
希望イメージ
シンプル 複雑
単色 カラフル
暗い 明るい
日常 高級
遊び心 厳粛
未来的 伝統的
女性的 男性的
希望する色
赤系、緑系、グレー系

```html
<!DOCTYPE html>
<html lang="ja">
<head>
<meta charset="utf-8">
<title>ポルネット本町店 無料体験チラシ</title>
<link href="https://fonts.googleapis.com/css2?family=Noto+Sans+JP:wght@400;500;700;900&display=swap" rel="stylesheet">
<style>
:root{
  --green:#2f9a3a;
  --green-dark:#1f7a2c;
  --green-pale:#e6f2df;
  --orange:#f08a12;
  --orange-dark:#e06a00;
  --text:#333;
  --grey:#c9c9c9;
  --white:#fff;
}
*{margin:0;padding:0;box-sizing:border-box}
html,body{width:849px;height:1200px;overflow:hidden;background:#fff}
body{font-family:"Noto Sans JP",sans-serif;color:var(--text)}
.flyer{position:relative;width:849px;height:1200px;overflow:hidden;background:var(--white)}
.abs{position:absolute}

.lead{left:0;top:22px;width:100%;text-align:center;color:var(--green);font-weight:900;font-size:40px;letter-spacing:2px}
.lead .big{font-size:56px}

.hero-title{left:0;top:105px;width:100%;text-align:center;color:var(--green);font-weight:900;font-size:140px;line-height:1;letter-spacing:6px}
.laurel{top:120px;width:90px;height:150px;border-radius:50%;background:var(--green-pale)}
.laurel.left{left:45px}
.laurel.right{right:45px}

.intro{left:0;top:268px;width:100%;text-align:center}
.intro span{display:inline-block;background:var(--green);color:#fff;font-weight:700;font-size:21px;padding:4px 26px}

.photo{left:0;top:310px;width:849px;height:400px;background:linear-gradient(180deg,#dfe8e4 0%,#b7cfb0 35%,#6fa352 60%,#4f8a35 100%)}
.partner{left:110px;top:345px;background:var(--green-dark);color:#fff;font-weight:700;font-size:26px;padding:4px 14px}
.round{left:110px;top:392px;background:var(--green);color:#fff;font-weight:900;font-size:64px;padding:2px 22px;line-height:1.3}
.save{left:110px;top:500px;color:#fff;font-weight:500;font-size:19px;text-shadow:0 1px 3px rgba(0,0,0,.45)}

.lesson-photo{left:40px;top:725px;width:205px;height:175px;background:linear-gradient(135deg,#6c8a73,#2f4a3a)}
.points{left:272px;top:730px;width:545px;list-style:none}
.points li{display:flex;align-items:center;font-weight:700;font-size:17px;letter-spacing:-0.3px;white-space:nowrap;color:var(--text);height:56px;border-bottom:1px dashed #bbb}
.points .num{flex:none;width:34px;height:34px;border-radius:50%;border:2px solid var(--orange);color:var(--orange);font-size:18px;display:flex;align-items:center;justify-content:center;margin-right:12px}

.campaign{left:40px;top:925px;width:770px;height:100px;border:3px solid var(--orange)}
.campaign-label{left:40px;top:920px;background:var(--orange);color:#fff;font-weight:900;font-size:30px;padding:2px 18px;white-space:nowrap}
.campaign-note{left:430px;top:932px;font-weight:700;font-size:18px;color:var(--text);white-space:nowrap}
.campaign-offer{left:54px;top:972px;width:744px;height:44px;font-weight:700;font-size:18px;color:var(--orange-dark);display:flex;align-items:baseline;justify-content:space-between;white-space:nowrap}
.campaign-offer .deadline{display:flex;align-items:baseline;gap:4px;color:var(--text)}
.campaign-offer .year{font-size:20px;font-weight:900}
.campaign-offer .date{font-weight:900;font-size:38px;line-height:1}
.campaign-offer .until{font-size:20px;color:var(--orange-dark)}

.tel{left:40px;top:1040px;display:flex;align-items:center;gap:8px;color:var(--orange-dark);font-weight:900;font-size:52px;letter-spacing:1px;line-height:1}
.tel-note{left:40px;top:1098px;font-size:11px;color:#555;width:500px}
.shop{left:40px;top:1114px;display:flex;align-items:center;gap:10px}
.shop-mark{width:22px;height:22px;border-radius:50%;background:var(--green)}
.shop-brand{font-weight:900;font-size:24px;color:var(--green)}
.shop-name{font-weight:900;font-size:26px;color:var(--text);margin-left:8px}
.info{left:40px;top:1146px;font-size:11px;line-height:1.5;color:#444;width:510px}
.info b{display:inline-block;background:var(--green);color:#fff;font-weight:700;padding:0 4px;margin-right:4px;font-size:10px}

.map{left:555px;top:1035px;width:280px;height:156px;background:var(--grey);display:flex;align-items:center;justify-content:center;color:#fff;font-weight:700;font-size:30px;letter-spacing:2px}
</style>
</head>
<body>
<div class="flyer">
  <p class="abs lead">今までなかった <span class="big">新ゴルフスタジオ</span></p>
  <div class="abs laurel left" role="img" aria-label="月桂樹の飾り"></div>
  <div class="abs laurel right" role="img" aria-label="月桂樹の飾り"></div>
  <h1 class="abs hero-title">無料体験</h1>
  <p class="abs intro"><span>神戸エリアにお住まいのあなたへの特別なご案内です。</span></p>

  <div class="abs photo" role="img" aria-label="ゴルフ場でスイングするゴルファーの写真"></div>
  <p class="abs partner">提携ゴルフ場がプレーフィが無料</p>
  <p class="abs round">ラウンドし放題</p>
  <p class="abs save">今年のラウンドフィを20万円以上も節約できるかもしれません。</p>

  <div class="abs lesson-photo" role="img" aria-label="ゴルフレッスンの様子の写真"></div>
  <ol class="abs points">
    <li><span class="num">1</span>提携ゴルフスタジオが無料でラウンドし放題</li>
    <li><span class="num">2</span>三宮初の通い放題ゴルフスタジオ。レッスンも練習も好きなだけ</li>
    <li><span class="num">3</span>レッスン上達実績多数の「スイングゾーン」理論採用</li>
  </ol>

  <div class="abs campaign"></div>
  <p class="abs campaign-label">２ヶ月無料キャンペーン</p>
  <p class="abs campaign-note">「このチラシを見た！」とお伝えください。</p>
  <p class="abs campaign-offer">
    <span>実質２万円のスタジオを２ヶ月間タダで使い放題！？</span>
    <span class="deadline"><span class="year">2019年</span><span class="date">0月00日</span><span class="until">まで</span></span>
  </p>

  <p class="abs tel">
    <svg width="42" height="42" viewBox="0 0 24 24" aria-hidden="true"><path fill="#e06a00" d="M6.6 10.8a15.1 15.1 0 0 0 6.6 6.6l2.2-2.2a1 1 0 0 1 1-.25 11.4 11.4 0 0 0 3.6.57 1 1 0 0 1 1 1V20a1 1 0 0 1-1 1A17 17 0 0 1 3 4a1 1 0 0 1 1-1h3.5a1 1 0 0 1 1 1c0 1.250.2 2.450.57 3.570a1 1 0 0 1-.25 1z"/></svg>
    078-415-3728
  </p>
  <p class="abs tel-note">※お一人様一回限り。ご予約はお電話にて承ります。詳しくは店頭でご確認ください。</p>
  <div class="abs shop">
    <span class="shop-mark"></span><span class="shop-brand">ポルネット</span><span class="shop-name">ポルネット本町店</span>
  </div>
  <p class="abs info">
    <b>定休日</b>火曜日　<b>営業時間</b>月曜日~木曜日10:00~22:00 / 金曜日~日曜日10:00~18:00<br>
    〒650-0011 兵庫県神戸市中央区下山手通5丁目8−21 ORB508ビル B1<br>
    ホームページ：https://polnetto-example.com
  </p>
  <div class="abs map" role="img" aria-label="店舗周辺の地図">MAP</div>
</div>
</body>
</html>
```